website design + images

We need a very appealing website design, layout and images for a sales analytics and sales productivity services company based in San Ramon, California. We need a good design for the home page and a template for all other pages (total 2 designs), and images for all inner pages (center column/banner images, and right hand top corner small images). There are about 18 inner pages.
Updates

Our existing website is www.vorlaxen.com
Our corporate colours are the ones that are there on the website. The logo is also shown. We will be changing the tagline to "accelerating revenue" or equivalent of that.

Please use the document "website for vorlaxen - template v2.doc" that I just uploaded for any reference to the content, navigation and wireframes. A few more clarifications are provided mainly for the link "Solutions".

Devendra Kothuri

Hi,
We just uploaded ver 4 of the website template. There is more elaboration provided around the sublinks / sections for Solutions. Pls review and do get back if you need any clarifications.

Rgds
Devendra Kothuri

Hi all,
We have so far received a few good designs. The designs are more or less on the right track. I would like to urge all of you to use the content and navigation provided in the document attached to our brief "website for vorlaxen - template v4.doc".  Please DO NOT use the content in our existing website www.vorlaxen.com . That is very old. We mentioned it only for reference to colour theme and broad details.

We have totally 13 sections in Solutions pages. They may be designed as a tree of links - first level sublinks - second level sublinks or links - first level sublinks and the remaining as sections within the first level sublinks pages. The page design would remain the same for all inner pages except careers. But after finalizing the design for the inner page, we will need images for the different inner pages.

Rgds
Devendra Kothuri

Hi,
Thank you all for participation and very good designs. We are quite happy with what we have seen. We have now shortlisted about 4 vendors and sending invididual feedback to them for further improvement. We will be finalizing by Monday or Tuesday.  To the vendors who do not get feedback from us, thank you very much for participation. We may still do business in future for some of our other needs. 
The following are the process steps / expectations going forward, 
1. Feedback to the shortlisted designers and inviting improvements.
2. Review of the improved designs and further shortlist & feedback or direct finalization.
3. The design should be in 1024*768
2. Number of page designs = 2 (home page, inner page).
4. Home page design: instead of delivery model and customers, show one link "Why Us".
4. Solutions page design:  We will be needing an image in center column of solutions page that in a nutshell gives all the different types of solutions we provide. The entire set of solutions is in our attached document website for vorlaxen - template v4 and I am just uploading v5 with more description on sublinks.
5. After selection, we will be needing images for all the solution pages (total 12 pages under solutions + one solutions page), 1 image for Why Us?, 1 for Careers, and 3 for company (about us/ team, core values, ...) = total 18

Rgds
Devendra Kothuri

Target Market(s)

We are a sales analytics and sales productivity services company. We help B2B companies with: sales planning; sales operations and sales measurement. The characteristics of our customers are:
- B2B medium enterprises (USD 100M- USD 2B in revenue) in the US
- Primary target verticals are: high-tech, engineering and professional services firms
- Our primary target customers titles are VP of Sales or VP of marketing; we could be selling to the CEO at companies with revenues below $200M

Industry/Entity Type

Consulting

Requirements
Must have
• - Clean, uncluttered design
• - Easy navigation; minimum clicks
Nice to have
• We have already built a content management system and wireframes for this site. To the extent possible, it would be great to leverage the wireframe structure we built, provided you don’t have to compromise on the look and feel and navigation of the site. Below is what we currently have as banner sizes and resolutions are:
• Home page banner size: 950 * 250’
• All pages – center top - image size: 558 * 160
• All pages – right hand top image – 175*135’

```html
<!DOCTYPE html>
<html lang="en">
<head>
<meta charset="utf-8">
<title>Vorlaxen – Home</title>
<link rel="stylesheet" href="https://fonts.googleapis.com/css2?family=Arimo:ital,wght@0,400;0,700;1,400&display=swap">
<style>
  :root {
    --page-bg: #f0f0f0;
    --panel-bg: #ffffff;
    --brand-blue: #0a68b4;
    --brand-green: #3f9a3a;
    --accent-orange: #f39a12;
    --text-grey: #8a8a8a;
    --nav-grey: #9a9a9a;
    --tile-bg: #efefef;
    --shadow: rgba(0, 0, 0, 0.28);
  }
  * { box-sizing: border-box; margin: 0; padding: 0; }
  html, body { width: 1200px; height: 900px; overflow: hidden; }
  body {
    background: var(--page-bg);
    font-family: "Arimo", Arial, sans-serif;
    position: relative;
  }
  .site-header {
    position: absolute; left: 41px; top: 0; width: 1113px; height: 124px;
    background: var(--panel-bg);
  }
  .brand {
    position: absolute; left: 27px; top: 40px;
    display: flex; align-items: center; gap: 10px;
  }
  .brand-dot { width: 22px; height: 22px; border-radius: 50%; background: var(--brand-blue); }
  .brand-name { font-size: 30px; font-weight: 400; color: var(--brand-blue); letter-spacing: 3px; }
  .utility-links {
    position: absolute; right: 42px; top: 18px;
    font-size: 14px; color: var(--nav-grey);
  }
  .main-nav {
    position: absolute; left: 332px; right: 40px; top: 100px;
    display: flex; justify-content: space-between;
    font-size: 13px; font-weight: 700;
  }
  .main-nav a { color: var(--nav-grey); text-decoration: none; }
  .main-nav a.is-current { color: var(--brand-blue); }

  .hero {
    position: absolute; left: 41px; top: 124px; width: 1113px; height: 293px;
    background: linear-gradient(100deg, #0a63b5 0%, #3a8ad0 40%, #7fb5e2 75%, #a9cdee 100%);
    box-shadow: 0 3px 5px var(--shadow);
  }
  .hero-photo {
    position: absolute; right: 0; bottom: 0; width: 640px; height: 160px;
    background: linear-gradient(180deg, rgba(255,255,255,0) 0%, rgba(200,215,230,0.55) 100%);
  }
  .hero-title {
    position: absolute; left: 27px; top: 88px;
    color: #fff; font-size: 28px; font-weight: 700;
  }
  .hero-sub {
    position: absolute; left: 27px; top: 124px;
    color: #fff; font-size: 21px;
  }

  .panel {
    position: absolute; top: 443px; height: 371px;
    background: var(--panel-bg);
    box-shadow: 0 3px 5px var(--shadow);
  }
  .panel-main { left: 41px; width: 786px; }
  .panel-side { left: 850px; width: 302px; }

  .section-heading {
    position: absolute; top: 50px;
    display: flex; justify-content: space-between; align-items: flex-end;
    border-bottom: 1px solid var(--brand-blue);
    color: var(--brand-blue); font-size: 14px; font-weight: 700;
    padding-bottom: 2px;
  }
  .section-heading .arrow { font-size: 18px; line-height: 16px; }
  .intro .section-heading { left: 27px; width: 307px; }
  .intro-text {
    position: absolute; left: 27px; top: 80px; width: 310px;
    color: var(--text-grey); font-size: 14px; line-height: 21px;
    white-space: nowrap;
  }
  .intro-text p + p { margin-top: 21px; }
  .read-more {
    position: absolute; font-size: 12px; font-weight: 700;
    color: var(--brand-blue); text-decoration: none;
  }
  .intro .read-more { left: 235px; top: 318px; }

  .service-tile {
    position: absolute; top: 38px; width: 129px; height: 176px;
    background: var(--tile-bg);
  }
  .service-tile.planning { left: 360px; }
  .service-tile.operations { left: 500px; }
  .service-tile.measurement { left: 641px; }
  .tile-photo { height: 84px; }
  .planning .tile-photo { background: linear-gradient(135deg, #cfd8dc, #7d9aa8); }
  .operations .tile-photo { background: linear-gradient(135deg, #e8eef0, #9fc3a3); }
  .measurement .tile-photo { background: linear-gradient(135deg, #f2f2f2, #b9bfc6); }
  .tile-label {
    padding: 6px 7px; font-size: 14px; font-weight: 700; line-height: 16px;
  }
  .planning .tile-label { color: var(--brand-blue); }
  .operations .tile-label { color: var(--brand-green); }
  .measurement .tile-label { color: var(--accent-orange); }

  .testimonial .section-heading { left: 13px; width: 251px; }
  .quote {
    position: absolute; left: 36px; top: 120px; width: 240px;
    color: var(--brand-green); font-size: 16px; font-style: italic; line-height: 21px;
    white-space: nowrap;
  }
  .quote-author {
    position: absolute; left: 36px; top: 272px;
    color: var(--brand-blue); font-size: 12px; font-weight: 700; line-height: 19px;
  }
  .testimonial .read-more { left: 170px; top: 316px; }

  .site-footer {
    position: absolute; left: 41px; top: 836px; width: 1113px; height: 41px;
    background: var(--panel-bg);
    box-shadow: 0 3px 5px var(--shadow);
    font-size: 12px; font-style: italic; color: var(--text-grey);
    display: flex; align-items: center; justify-content: flex-end; padding-right: 43px;
  }
</style>
</head>
<body>
  <header class="site-header">
    <div class="brand">
      <span class="brand-dot"></span>
      <span class="brand-name">VORLAXEN</span>
    </div>
    <div class="utility-links">Sitemap | Sign in / Register | Contact us</div>
    <nav class="main-nav">
      <a href="#" class="is-current">HOME</a>
      <a href="#">SOLUTIONS</a>
      <a href="#">WHY US?</a>
      <a href="#">COMPANY</a>
      <a href="#">CAREERS</a>
    </nav>
  </header>

  <section class="hero">
    <div class="hero-photo" role="img" aria-label="Relaxed businessman leaning back with feet on a desk beside a laptop under a blue sky"></div>
    <h1 class="hero-title">Lorem ipsum dolor sit amet.</h1>
    <p class="hero-sub">consectetur adipiscing elit.</p>
  </section>

  <section class="panel panel-main">
    <div class="intro">
      <h2 class="section-heading"><span>INTRODUCTION</span><span class="arrow">&gt;</span></h2>
      <div class="intro-text">
        <p>At Vorlaxen, we deliver solutions to improve<br>sales productivity and marketing effectiveness<br>of high-tech, engineering, and professional<br>services firms.</p>
        <p>Our customers lead corporate<br>marketing, product marketing, channel<br>marketing, sales operations, sales<br>management and IT functions at their<br>organizations.</p>
      </div>
      <a class="read-more" href="#">&gt;&gt; read more...</a>
    </div>
    <div class="service-tile planning">
      <div class="tile-photo" role="img" aria-label="Hand with pen reviewing charts on a screen"></div>
      <div class="tile-label">SALES<br>PLANNING<br>ANALYTICS</div>
    </div>
    <div class="service-tile operations">
      <div class="tile-photo" role="img" aria-label="Support consultant working at a laptop"></div>
      <div class="tile-label">SALES<br>OPERATIONS<br>SUPPORT</div>
    </div>
    <div class="service-tile measurement">
      <div class="tile-photo" role="img" aria-label="Pen resting on printed line charts"></div>
      <div class="tile-label">SALES<br>MEASUREMENT<br>ANALYTICS</div>
    </div>
  </section>

  <aside class="panel panel-side testimonial">
    <h2 class="section-heading"><span>CUSTOMER TESTIMONIAL</span><span class="arrow">&gt;</span></h2>
    <blockquote class="quote">Aliquam eros leo, pretium at<br>imperdiet id, fringilla at velit.<br>Donec pellentesque mollis<br>massa eu porttitor. Aliquam<br>risus metus, placerat at<br>ornare id</blockquote>
    <p class="quote-author">Name Person<br>Meridane</p>
    <a class="read-more" href="#">&gt;&gt; read more...</a>
  </aside>

  <footer class="site-footer">© 2008 Vorlaxen, Inc. | Disclaimer</footer>
</body>
</html>
```